UK based media owner KELVANO (http://www.kelvano.uk/) needs DIGITAL ADVERT to run on our digital panel

Hi guys,

Thanks for taking the time to have a look at this brief.
I need someone to create a digital advert (still/static design or video) to run on our digital panels which are located across UK university student unions.
For who wants to upload a video ---> All of our panels are digitally enabled and allow for full motion video – they run adverts 10 seconds long (see artwork specification document in attachment) therefore the advert will have to be 10 seconds long.
For static/still design ----> see artwork specification to see resolution etc

I need something professional looking, polished yet fresh and exciting so that it speaks and connects to this younger audience – we want to inspire them to take a step towards new levels of business opportunities.

Here are some Key Points you’ll need to take into consideration when designing the advert:

Overall Campaign Objective: To excite and attract young entrepreneurs to get in touch with us for possible partnerships

Target Audience: Young entrepreneurs attending university (university students – 18 to 24 years old)

Creative Specifications: See attached document with artwork specifications

Text on Advert:

I need the following text to appear on the advert: (Please include company logo)

“Do you have a business idea that would benefit with advertising on these screens?

We want to support young entrepreneurs and will partner with any whom have a great idea

WE WANT TO HEAR FROM YOU!

Email us at ideas@kelvano.uk
www.kelvano.uk/ideas”

I would need some ideas by the 3rd July 2018 if possible.

Thanks to all who will take part in this project – contact me if you have any questions

Target Market(s)

Young entrepreneurs attending university (university students – 18 to 24 years old)

Requirements
Must have
• I need the following text to appear on the advert: (Please include company logo)
• “Do you have a business idea that would benefit with advertising on these screens?
• We want to support young entrepreneurs and will partner with any whom have a great idea
• WE WANT TO HEAR FROM YOU!
• Email us at ideas@kelvano.uk
• www.kelvano.uk/ideas”

```html
<!DOCTYPE html>
<html lang="en">
<head>
<meta charset="utf-8">
<title>KELVANO – Business Ideas Panel Advert</title>
<link rel="stylesheet" href="https://fonts.googleapis.com/css2?family=Open+Sans:wdth,wght@75..100,300..800&display=swap">
<style>
  :root {
    --brand-red: #b11226;
    --sun-yellow: #f8ea5c;
    --cool-grey: #c9c9c9;
    --sky-blue: #4fc3ec;
    --headline-blue: #5bbde8;
    --ink-grey: #474747;
    --white: #ffffff;
  }
  html, body {
    margin: 0;
    padding: 0;
    overflow: hidden;
    background: #ffffff;
  }
  .panel {
    position: relative;
    width: 675px;
    height: 1200px;
    overflow: hidden;
    font-family: "Open Sans", Arial, sans-serif;
    font-stretch: 75%;
    background: var(--cool-grey);
  }
  .top-band, .bottom-band {
    position: absolute;
    left: 0;
    width: 675px;
    background: var(--brand-red);
    z-index: 2;
  }
  .top-band { top: 0; height: 68px; }
  .bottom-band { top: 1136px; height: 64px; }
  .web-address {
    position: absolute;
    right: 42px;
    top: 18px;
    margin: 0;
    color: var(--white);
    font-size: 23px;
    font-weight: 400;
    font-stretch: 100%;
    letter-spacing: 0.5px;
  }
  .brand-name {
    position: absolute;
    right: 40px;
    top: 0;
    margin: 0;
    color: var(--white);
    font-size: 40px;
    font-weight: 400;
    font-stretch: 100%;
    line-height: 64px;
    letter-spacing: 11px;
  }
  .block-yellow {
    position: absolute;
    left: 0; top: 68px;
    width: 338px; height: 330px;
    background: var(--sun-yellow);
  }
  .student-photo {
    position: absolute;
    left: 338px; top: 68px;
    width: 337px; height: 330px;
    background: linear-gradient(160deg, #fbf6b4 0%, #d8d38a 45%, #8f8a55 75%, #f2ecb0 100%);
  }
  .block-grey {
    position: absolute;
    left: 0; top: 398px;
    width: 675px; height: 738px;
    background: var(--cool-grey);
  }
  .block-blue {
    position: absolute;
    left: 338px; top: 696px;
    width: 337px; height: 440px;
    background: var(--sky-blue);
  }
  .headline-question {
    position: absolute;
    left: 50px;
    top: 190px;
    margin: 0;
    color: var(--headline-blue);
    font-size: 115px;
    font-weight: 700;
    line-height: 1;
    letter-spacing: -1px;
    white-space: nowrap;
  }
  .speech-bubble {
    position: absolute;
    left: 0; top: 0;
  }
  .bubble-text {
    position: absolute;
    left: 154px;
    top: 442px;
    width: 466px;
    margin: 0;
    text-align: center;
    color: var(--brand-red);
    font-size: 88px;
    font-weight: 700;
    line-height: 104px;
    letter-spacing: -1px;
  }
  .benefit-line {
    position: absolute;
    margin: 0;
    color: var(--ink-grey);
    font-size: 58px;
    font-weight: 700;
    line-height: 1;
    letter-spacing: -1px;
    white-space: nowrap;
  }
  .benefit-line.first { left: 48px; top: 824px; }
  .benefit-line.second { right: 54px; top: 896px; }
  .call-out {
    position: absolute;
    left: 78px;
    top: 1005px;
    margin: 0;
    color: var(--brand-red);
    font-size: 71px;
    font-weight: 700;
    line-height: 1;
    letter-spacing: -1px;
    white-space: nowrap;
  }
</style>
</head>
<body>
<main class="panel">
  <div class="top-band">
    <p class="web-address">www.kelvano.uk/ideas</p>
  </div>

  <div class="block-yellow"></div>
  <div class="student-photo" role="img" aria-label="Photo of a young student entrepreneur on the phone, tinted pale yellow"></div>
  <div class="block-grey"></div>
  <div class="block-blue"></div>

  <h1 class="headline-question">Do you have</h1>

  <svg class="speech-bubble" width="675" height="1200" viewBox="0 0 675 1200" aria-hidden="true">
    <path d="M196 402 H580 Q620 402 620 442 V660 Q620 700 580 700 H516 V796 L392 700 H196 Q154 700 154 660 V442 Q154 402 196 402 Z"
          fill="none" stroke="#b11226" stroke-width="24" stroke-linejoin="round"/>
  </svg>

  <p class="bubble-text">...a business<br>idea...</p>

  <p class="benefit-line first">...that would benefit</p>
  <p class="benefit-line second">with advertising...</p>

  <p class="call-out">ON THESE SCREENS?</p>

  <div class="bottom-band">
    <p class="brand-name">KELVANO</p>
  </div>
</main>
</body>
</html>
```